Events and Parties web-site needs a Web Design

VoTrel needs a web design.
VoTrel means The Bees in Italian.
VoTrel target market is people who is organizing parties and events.
Our mission is that the parties and events of our clients exceed their expectations by providing them web and mobile tools.
Our vision is to be the best and biggest party web portal of the country.
The main features of our web site is to let people invite guests and search suppliers/providers. Guests will also confirm presence (RSVP) and buy presents/gifts at the site as well.
Our slogan is "Curta sua festa desde já !" that means "Enjoy our party now !" in Brazilian Portuguese.
The idea here is that the party starts now and not only at the scheduled date and time.
Updates
It seems that must have and nice to have briefing is not appearing to you as I filled. So I will type it agai here:
Our slogan text that is "Curta sua festa desde já !" that means "Enjoy your party now !".
Space to paid ads.
Language switch to Spanish. Brazilian Portuguese is our default language.
Logon form with 2 inputs: Email and password.
RSVP form with 2 inputs: Event ID and password
Kendro trusted site seal (SSL/HTTPS) logo.
Update to my briefing: Only event organizer and guests will be able to see details of the events/parties like photos/blog, guest list and etc. Suppliers will be searched and rated like stayvoro.com/roamgliq.
Target Market(s)
VoTrel target market is amateur and professional people who are organizing parties and events.
Our mission is that the parties and events of our clients exceed their expectations by providing them easy and fast web and mobile tools.
Our vision is to be the best and biggest party portal of our country.
The main features of our web site is to let people invite guests and search suppliers/providers. Guests will also confirm presence (RSVP) and buy presents at the site.
Industry/Entity Type
Events
Requirements
Must have
- Design and colors compliant with attached logo.
- Our slogan text that is "Curta sua festa desde já !" that means "Enjoy your party now !".
- Space to paid ads.
- Language switch to Spanish. Brazilian Portuguese is our default language.
- Logon form with 2 inputs: Email and password.
- RSVP form with 2 inputs: Event ID and password
- Kendro trusted site seal (SSL/HTTPS) logo.
Nice to have
- VoTrel stands for The Bees in Italian. It would be very nice to have a not so explicit idea that each user is a bee and VoTrel is the hive where party/event occurs.
Should not have
- No PageMill please.
- No infant/child oriented designs please. Our market is not only children birthdays but also other parties and events like marriages, corporate events and so on

```html
<!DOCTYPE html>
<html lang="pt-BR">
<head>
<meta charset="utf-8">
<title>VoTrel – Curta sua festa desde já!</title>
<link rel="stylesheet" href="https://fonts.googleapis.com/css2?family=Open+Sans:ital,wght@0,300;0,400;0,700;1,300;1,400;1,700&display=swap">
<style>
  :root {
    --honey: #ffce5a;
    --honey-deep: #ffc846;
    --amber: #ffa544;
    --brown: #330a05;
    --orange: #f68b1f;
    --panel: #e9e5e4;
    --white: #ffffff;
    --green: #3d9662;
    --lime: #80bb3f;
    --ad-border: #b44ee0;
  }
  * { box-sizing: border-box; margin: 0; padding: 0; }
  html, body { width: 1200px; height: 1091px; overflow: hidden; background: var(--white); }
  body { font-family: "Open Sans", sans-serif; color: var(--brown); position: relative; }

  .site-header { position: absolute; left: 0; top: 0; width: 1200px; height: 193px; background: var(--honey); }
  .brand { position: absolute; left: 0; width: 1200px; top: 58px; text-align: center; }
  .brand-mark { display: inline-block; width: 54px; height: 54px; border-radius: 50%; background: var(--brown); vertical-align: middle; margin-right: 14px; }
  .brand-name { font-size: 56px; font-weight: 400; color: var(--brown); vertical-align: middle; }

  .lang-switch { position: absolute; left: 993px; top: 18px; width: 98px; height: 24px; border-radius: 5px; background: #f3c04e; font-size: 12px; line-height: 24px; padding-left: 31px; }
  .lang-flag { position: absolute; left: 10px; top: 6px; width: 17px; height: 12px; background: #2f9a42; border-radius: 1px; }

  .slogan { position: absolute; left: 107px; top: 224px; width: 570px; font-size: 45px; line-height: 60px; font-weight: 300; font-style: italic; letter-spacing: -0.5px; white-space: nowrap; }

  .ad { position: absolute; border: 1px solid var(--ad-border); display: flex; align-items: center; justify-content: center; text-align: center; font-weight: 700; font-style: italic; }
  .ad-leader { left: 689px; top: 212px; width: 402px; height: 87px; font-size: 25px; color: rgba(190, 110, 220, .75);
    background: radial-gradient(ellipse at 30% 20%, #ffd2ff 0%, #f6b6ff 50%, #e189ff 100%); }
  .ad-box { left: 764px; top: 657px; width: 327px; height: 272px; font-size: 27px; line-height: 1.35; color: rgba(170, 60, 210, .85);
    background: radial-gradient(ellipse at 40% 40%, #ff66ff 0%, #f455ff 45%, #ff9cff 75%, #ffffff 100%); }

  .panel { position: absolute; top: 317px; width: 464px; height: 310px; background: var(--panel); border-radius: 26px; overflow: hidden; }
  .panel-login { left: 109px; }
  .panel-rsvp { left: 627px; }
  .panel-head { height: 65px; padding-left: 38px; line-height: 72px; font-size: 25px; font-weight: 700; font-style: italic; }
  .panel-login .panel-head { background: var(--honey-deep); }
  .panel-rsvp .panel-head { background: var(--amber); }
  .field { position: absolute; left: 32px; width: 400px; height: 56px; border-radius: 10px; background: var(--white); padding-left: 22px; line-height: 56px; font-size: 18px; color: var(--orange); }
  .field-1 { top: 84px; }
  .field-2 { top: 158px; }
  .forgot { position: absolute; left: 53px; top: 252px; font-size: 13px; }
  .btn { position: absolute; left: 273px; top: 231px; width: 159px; height: 56px; border-radius: 10px; color: var(--white); text-align: center; line-height: 58px; font-size: 24px; font-weight: 700; font-style: italic; }
  .panel-login .btn { background: var(--green); }
  .panel-rsvp .btn { background: var(--lime); }

  .or { position: absolute; left: 584px; top: 328px; font-size: 32px; font-weight: 300; font-style: italic; }

  .content { position: absolute; left: 107px; top: 645px; width: 620px; }
  .content-title { font-size: 26px; font-weight: 700; font-style: italic; color: var(--orange); margin-bottom: 4px; }
  .content p { font-size: 15.2px; line-height: 28.4px; padding-left: 2px; margin-bottom: 28.4px; }
</style>
</head>
<body>
  <header class="site-header">
    <div class="brand"><span class="brand-mark"></span><span class="brand-name">VoTrel</span></div>
    <div class="lang-switch"><span class="lang-flag"></span>Language</div>
  </header>

  <h1 class="slogan">Curta sua festa desde já!</h1>
  <div class="ad ad-leader" role="img" aria-label="Paid banner advertisement space">368x80 Banner Ad</div>

  <section class="panel panel-login">
    <div class="panel-head">LOG IN</div>
    <div class="field field-1">Email...</div>
    <div class="field field-2">Password...</div>
    <div class="forgot">Forgotten Password</div>
    <div class="btn">SIGN IN</div>
  </section>

  <div class="or">or</div>

  <section class="panel panel-rsvp">
    <div class="panel-head">RSVP</div>
    <div class="field field-1">Event ID...</div>
    <div class="field field-2">Password...</div>
    <div class="forgot">Forgotten Password</div>
    <div class="btn">RSVP</div>
  </section>

  <article class="content">
    <h2 class="content-title">This where you put the content title</h2>
    <p>Lorem ipsum dolor sit amet, dico quaerendum mel cu, has ei cibo nonumy officiis, vim ancillae mentitum id. His ea scaevola platonem delicata, atqui minim verear duo in. Possim ponderum perpetua ea vim, est veri suscipit consequat no, saepe docendi consulatu per cu. Sed fugit sonet insolens cu, pro ex veri saepe.</p>
    <p>Nec at vero sonet quaeque, ius vivendum legendos no. Vix id semper essent, nec ut movet scaevola. Cu cibo natum dissentiunt usu, ex ius suscipit platonem splendide. Doctus sanctus forensibus sed an, elit recusabo sed in. Timeam principes iracundia ea ius, te mel habeo fugit vitae.</p>
  </article>

  <div class="ad ad-box" role="img" aria-label="Paid square banner advertisement space">300x250<br>Banner Ad</div>
</body>
</html>
```